10 Page Marketing Report Template - Cindermoor Care Allies

https://www.vidquill.example/share/7f1e9c04b2d84a61a5c3e9d02b6f4a17

We are creating a professional, modern, and slightly edgy PDF-style report document (about 10 pages) to showcase the results of a client’s first 30 days with Cindermoor Care Allies.

The report will be designed as a customizable Plakkit template so the Client Success team can easily update logos, screenshots, and text for each client.

This document will serve as both a visual presentation piece and a report deliverable, blending clean design, modern layout, and data-driven storytelling.

I am attaching the content for the report doc and the design brief along with the logo.
Here is our website for design style, look, and feel: https://cindermoorcare.example/

Here is a quick overview video I made:

```html
<!DOCTYPE html>
<html lang="en">
<head>
<meta charset="utf-8">
<title>30 Days to Value Report – Cindermoor Care Allies</title>
<link href="https://fonts.googleapis.com/css2?family=Oswald:wght@400;500;600;700&family=Lato:wght@400;700&display=swap" rel="stylesheet">
<style>
:root{
  --stage:#3d3d3f;
  --navy:#1b2a4e;
  --navy-deep:#0e1a3a;
  --sky:#5b93cf;
  --sky-light:#7fb0e0;
  --gold:#f2a922;
  --paper:#ffffff;
  --paper-grey:#eeeff1;
  --ink:#2a2f3a;
  --muted:#5a6070;
  --heading-blue:#3f7fc4;
}
*{box-sizing:border-box;margin:0;padding:0}
html,body{width:1200px;height:474px;overflow:hidden;background:var(--stage)}
body{position:relative;font-family:"Lato",sans-serif;color:var(--ink)}
.page-label{position:absolute;top:32px;width:255px;text-align:center;color:#fff;font-family:"Lato",sans-serif;font-size:16px}
.page{position:absolute;top:71px;width:255px;height:357px;overflow:hidden;background:var(--paper)}
.band{position:absolute;left:0;top:318px;width:255px;height:24px}
.band-url{position:absolute;left:18px;top:331px;font-size:5.6px;color:#fff;letter-spacing:.1px}
.brand{display:flex;align-items:center;gap:5px;font-family:"Lato",sans-serif;font-weight:700;letter-spacing:.3px}
.brand-mark{width:9px;height:9px;background:var(--gold);flex:none}
.tagline{font-size:4.2px;letter-spacing:.6px;margin-top:3px}

/* cover */
.cover{left:53px;background:var(--navy-deep)}
.cover-art{position:absolute;inset:0;background:radial-gradient(ellipse at 60% 40%,#2a6fd0 0%,#13306e 38%,#0b1736 75%)}
.cover .brand{position:absolute;left:29px;top:32px;color:#fff;font-size:7.5px;width:110px;line-height:1.1}
.cover .tagline{position:absolute;left:29px;top:56px;color:#fff}
.cover-title{position:absolute;left:29px;top:142px;font-family:"Oswald",sans-serif;font-weight:700;line-height:.98}
.cover-title .days{display:block;color:var(--gold);font-size:30px}
.cover-title .rest{display:block;color:#fff;font-size:30px;letter-spacing:.2px}
.cover-sub{position:absolute;left:31px;top:203px;width:192px;height:20px;border:1px solid var(--sky-light);color:#fff;font-size:12px;line-height:18px;text-align:center}
.client-slot{position:absolute;left:29px;top:254px;width:66px;height:40px;background:#fff;color:#8a8f9a;font-style:italic;font-size:11px;line-height:.85;padding:5px 0 0 13px}
.cover-date{position:absolute;left:162px;top:287px;color:#fff;font-size:7.5px}

/* page 1 */
.overview{left:343px}
.hero-photo{position:absolute;left:0;top:0;width:255px;height:176px;background:linear-gradient(180deg,#b9c2cf 0%,#6a7891 45%,#1e2c52 75%,#1b2a4e 100%)}
.hero-lines{position:absolute;left:19px;top:98px;font-family:"Oswald",sans-serif;font-size:16.5px;line-height:21px;color:var(--sky-light)}
.hero-lines b{color:#fff;font-weight:600}
.overview-tab{position:absolute;left:0;top:177px;width:120px;height:12px;background:var(--sky);color:#fff;font-family:"Oswald",sans-serif;font-size:9.5px;line-height:12px;padding-left:36px}
.overview-text{position:absolute;left:26px;top:208px;width:205px;border-left:1px solid var(--navy);padding-left:8px;font-size:5.7px;line-height:7.3px;color:var(--ink)}
.overview-text p+p{margin-top:6px}
.overview .brand{position:absolute;left:90px;top:298px;color:var(--navy);font-size:5.6px;width:80px;line-height:1.1}
.overview .tagline{position:absolute;left:90px;top:313px;color:var(--navy);font-size:3.4px}

/* section headers */
.section-head{position:absolute;left:0;height:20px;background:var(--navy);color:#fff;font-family:"Oswald",sans-serif;font-weight:500;font-size:11.5px;line-height:20px;padding-left:19px;white-space:nowrap;clip-path:polygon(0 0,calc(100% - 14px) 0,100% 100%,0 100%)}
.section-head::after{content:"";position:absolute;right:0;top:0;width:16px;height:20px;background:var(--gold);clip-path:polygon(0 0,3px 0,16px 20px,13px 20px)}

/* page 2 */
.highlights{left:598px;background:var(--paper-grey)}
.wins{position:absolute;left:19px;top:52px;width:225px;display:grid;grid-template-columns:1fr 1fr;row-gap:6px;column-gap:8px}
.win{display:flex;align-items:center;gap:6px;font-size:5.8px;line-height:7px;color:var(--ink)}
.win svg{flex:none;width:14px;height:14px}
.audit-intro{position:absolute;left:19px;top:157px;width:220px;font-size:5.8px;line-height:7px}
.flow{position:absolute;left:19px;top:183px;width:220px;height:38px}
.deliv-head{position:absolute;left:28px;top:230px;color:var(--heading-blue);font-size:7.5px}
.deliv{position:absolute;left:19px;top:242px;width:225px;list-style:none;font-size:5.7px;line-height:6.6px}
.deliv li{position:relative;padding-left:9px;margin-bottom:4.2px}
.deliv li::before{content:"";position:absolute;left:0;top:1.6px;width:3.4px;height:3.4px;border-radius:50%;background:var(--gold)}
.deliv b{color:var(--navy)}

/* page 3 */
.progress{left:888px}
.summary-head{position:absolute;left:19px;top:57px;color:var(--heading-blue);font-size:7.5px}
.summary{position:absolute;left:19px;top:68px;width:220px;font-size:5px;line-height:6.2px}
.summary p+p{margin-top:6px}
.devices{position:absolute;left:19px;top:125px;width:170px;height:95px;background:linear-gradient(160deg,#2b3d78 0%,#1b2a4e 55%,#9aa3b0 100%);border-radius:4px}
.launched{position:absolute;left:100px;top:211px;width:155px;height:10px;background:var(--gold);color:var(--navy);font-size:7px;font-weight:700;line-height:10px;text-align:right;padding-right:42px}
.list-head{position:absolute;top:246px;color:var(--heading-blue);font-size:7.5px}
.tick-list{position:absolute;top:259px;list-style:none;font-size:5px;line-height:6px}
.tick-list li{position:relative;padding-left:9px;margin-bottom:6.2px}
.tick-list li::before{content:"";position:absolute;left:0;top:1.2px;width:3.4px;height:3.4px;border-radius:50%;background:var(--gold)}
</style>
</head>
<body>

<div class="page-label" style="left:53px">Cover</div>
<div class="page-label" style="left:343px">Page 1</div>
<div class="page-label" style="left:598px">Page 2</div>
<div class="page-label" style="left:888px">Page 3</div>

<!-- COVER -->
<section class="page cover">
  <div class="cover-art" role="img" aria-label="Glowing blue digital growth chart background with rising light lines"></div>
  <div class="brand"><span class="brand-mark"></span>CINDERMOOR CARE ALLIES</div>
  <div class="tagline">BUILDING REACH. RENEWING CARE.</div>
  <h1 class="cover-title"><span class="days">30 DAYS</span><span class="rest">TO VALUE REPORT</span></h1>
  <div class="cover-sub">Your First Month of Progress</div>
  <div class="client-slot">CLIENT<br>LOGO<br>HERE</div>
  <div class="cover-date">Date: DD/MM/YY</div>
  <svg class="band" viewBox="0 0 255 24" aria-hidden="true">
    <polygon points="0,6 200,6 206,0 255,0 255,8 0,8" fill="#2b3f72"/>
    <polygon points="0,6 125,6 118,20 0,20" fill="#5b93cf"/>
    <polygon points="195,8 255,8 255,15 190,15" fill="#5b93cf"/>
  </svg>
  <div class="band-url">https://cindermoorcare.example/</div>
</section>

<!-- PAGE 1 -->
<section class="page overview">
  <div class="hero-photo" role="img" aria-label="Business professionals shaking hands in a bright office"></div>
  <svg style="position:absolute;left:0;top:140px" width="255" height="45" aria-hidden="true">
    <polygon points="0,36 115,36 145,20 180,20 190,12 255,12 255,45 0,45" fill="#ffffff"/>
    <polyline points="118,36 148,20 182,20 192,12 255,12" fill="none" stroke="#f2a922" stroke-width="2"/>
  </svg>
  <div class="hero-lines">Live With <b>Integrity.</b><br>Serve With <b>Excellence.</b><br>Change The <b>World.</b></div>
  <div class="overview-tab">OVERVIEW</div>
  <div class="overview-text">
    <p>The first 30 days are about creating momentum. Our goal was to build the foundation for measurable growth — from your website and Findly Business Profile to your SEO systems, audits, and backlink strategy.</p>
    <p>This report highlights what’s been accomplished and what’s next in your marketing journey.</p>
  </div>
  <div class="brand"><span class="brand-mark" style="width:7px;height:7px"></span>CINDERMOOR CARE ALLIES</div>
  <div class="tagline">BUILDING REACH. RENEWING CARE.</div>
  <svg class="band" viewBox="0 0 255 24" aria-hidden="true">
    <polygon points="0,8 200,8 206,2 255,2 255,10 0,10" fill="#2b3f72"/>
    <polygon points="0,8 120,8 112,22 0,22" fill="#5b93cf"/>
  </svg>
  <div class="band-url">https://cindermoorcare.example/</div>
</section>

<!-- PAGE 2 -->
<section class="page highlights">
  <h2 class="section-head" style="top:24px;width:158px">Highlights &amp; Quick Wins</h2>
  <div class="wins">
    <div class="win"><svg viewBox="0 0 14 14"><rect x=".5" y=".5" width="13" height="13" rx="2" fill="#fff" stroke="#f2a922"/><circle cx="7" cy="7" r="3" fill="none" stroke="#f2a922"/></svg>Website launched and optimized for SEO</div>
    <div class="win"><svg viewBox="0 0 14 14"><rect x=".5" y=".5" width="13" height="13" rx="2" fill="#fff" stroke="#f2a922"/><path d="M4 10l6-6M6 4h4v4" fill="none" stroke="#f2a922"/></svg>Backlink strategy implementation underway</div>
    <div class="win"><svg viewBox="0 0 14 14"><rect x=".5" y=".5" width="13" height="13" rx="2" fill="#fff" stroke="#f2a922"/><circle cx="7" cy="6" r="2.5" fill="#f2a922"/><path d="M5 8l-1 3M9 8l1 3" stroke="#f2a922"/></svg>Findly Business Profiles verified and optimized</div>
    <div class="win"><svg viewBox="0 0 14 14"><rect x=".5" y=".5" width="13" height="13" rx="2" fill="#fff" stroke="#f2a922"/><path d="M4 10l6-6" stroke="#f2a922" stroke-width="1.5"/></svg>First blog articles published</div>
    <div class="win"><svg viewBox="0 0 14 14"><rect x=".5" y=".5" width="13" height="13" rx="2" fill="#fff" stroke="#f2a922"/><path d="M4 10l5-5M7 4l3 3" stroke="#f2a922"/></svg>Comprehensive SEO audits completed</div>
    <div class="win"><svg viewBox="0 0 14 14"><rect x=".5" y=".5" width="13" height="13" rx="2" fill="#fff" stroke="#f2a922"/><path d="M4 11V8M7 11V5M10 11V7" stroke="#f2a922" stroke-width="1.5"/></svg>Tracking and analytics systems connected</div>
  </div>
  <h2 class="section-head" style="top:128px;width:255px;font-size:10.6px;letter-spacing:-.1px">Comprehensive Audits &amp; Strategy Development</h2>
  <p class="audit-intro">To ensure long-term results, our team conducted a full suite of technical and strategic audits during the first month. These insights guided your SEO roadmap and content strategy moving forward.</p>
  <svg class="flow" viewBox="0 0 220 38" aria-hidden="true">
    <g fill="#1b2a4e" stroke="#9fc0e6" stroke-width="1.5">
      <circle cx="19" cy="19" r="17.5"/><circle cx="79" cy="19" r="17.5"/><circle cx="139" cy="19" r="17.5"/><circle cx="199" cy="19" r="17.5"/>
    </g>
    <g fill="none" stroke="#fff" stroke-width="1.6">
      <circle cx="19" cy="19" r="6"/><circle cx="19" cy="19" r="2.5"/>
      <circle cx="77" cy="17" r="5.5"/><path d="M81 21l5 5"/>
      <path d="M132 26V21M137 26V17M142 26V19M147 26V14"/>
      <circle cx="199" cy="19" r="8"/><circle cx="199" cy="19" r="4"/><path d="M199 19l8-8"/>
    </g>
    <g stroke="#5b93cf" stroke-width="1.5" fill="#5b93cf">
      <path d="M39 19h16"/><path d="M55 16l4 3-4 3z"/>
      <path d="M99 19h16"/><path d="M115 16l4 3-4 3z"/>
      <path d="M159 19h16"/><path d="M175 16l4 3-4 3z"/>
    </g>
  </svg>
  <div class="deliv-head">Audits &amp; Deliverables Completed:</div>
  <ul class="deliv">
    <li><b>Technical SEO Audit:</b> Site health, indexation, and crawl efficiency</li>
    <li><b>Backlink Audit:</b> Link quality, toxicity review, and authority scoring</li>
    <li><b>Competitor Analysis:</b> Top-ranking competitors’ content, backlinks, and keyword profiles</li>
    <li><b>On-Page SEO Audit:</b> Metadata, headings, internal links, and content structure</li>
    <li><b>Content Audit:</b> Keyword targeting, topical gaps, and conversion opportunities</li>
    <li><b>Strategy Development:</b> 90-day SEO plan and keyword roadmap created</li>
  </ul>
  <svg class="band" viewBox="0 0 255 24" aria-hidden="true">
    <polygon points="0,8 210,8 216,2 255,2 255,10 0,10" fill="#2b3f72"/>
    <polygon points="0,8 125,8 117,22 0,22" fill="#5b93cf"/>
    <polygon points="200,10 255,10 255,16 196,16" fill="#5b93cf"/>
  </svg>
  <div class="band-url">https://cindermoorcare.example/</div>
</section>

<!-- PAGE 3 -->
<section class="page progress">
  <h2 class="section-head" style="top:27px;width:130px">Website Progress</h2>
  <div class="summary-head">Summary</div>
  <div class="summary">
    <p>They specialise in marketing and consulting for addiction-treatment and behavioural-health organisations — especially rehab centres. Services include digital marketing: SEO, PPC/Findly Ads, web design, social media, content marketing.</p>
    <p>They also provide consulting to help treatment centres open/operate: licensing (state / accreditation like Meridian Standards Board / QARC), feasibility studies, financial proformas, business-planning.</p>
  </div>
  <div class="devices" role="img" aria-label="Laptop and phone showing the newly launched website"></div>
  <div class="launched">Launched Pages</div>
  <div class="list-head" style="left:28px">Optimizations Completed:</div>
  <ul class="tick-list" style="left:19px">
    <li>On-page SEO (titles, meta, H1s)</li>
    <li>Local schema added</li>
    <li>Call tracking integrated</li>
    <li>Mobile responsiveness reviewed</li>
  </ul>
  <div class="list-head" style="left:142px">Next Steps:</div>
  <ul class="tick-list" style="left:133px">
    <li>CRO improvements</li>
    <li>Additional service or location pages</li>
  </ul>
  <svg class="band" viewBox="0 0 255 24" aria-hidden="true">
    <polygon points="0,8 205,8 211,2 255,2 255,10 0,10" fill="#2b3f72"/>
    <polygon points="0,8 122,8 114,22 0,22" fill="#5b93cf"/>
    <polygon points="195,10 255,10 255,16 191,16" fill="#5b93cf"/>
  </svg>
  <div class="band-url">https://cindermoorcare.example/</div>
</section>

</body>
</html>
```